VELKORIS Stationery Design Project

I want a stationery design for a web development company consists of:
1- business card
2- Letter Head
3- small Envelope
4- Large Envelope

need a very clean professional simple design yet creative,

The company logo is attached
http://www.pixelbazaarhub.net/project-progress/designs.aspx?briefId=5830174&submissionId=47210938

logo font is sui generis rg (attached)
I would like to have the stationery text font to be helvetica font regular or light (can be changed)

I love the combination of cyan, black and grey colors
( will attach some recommended styles)

Business

• curves or waves

```html
<!DOCTYPE html>
<html lang="en">
<head>
<meta charset="utf-8">
<title>VELKORIS Presentation Folder</title>
<link href="https://fonts.googleapis.com/css2?family=Arimo:wght@400&display=swap" rel="stylesheet">
<style>
  :root {
    --stage: #d6d6d6;
    --stage-light: #ececec;
    --folder: #242424;
    --folder-edge: #1c1c1c;
    --cyan: #219bd3;
    --cyan-deep: #1d86b8;
    --ink-light: #c9c9c9;
    --url-ink: #bfe6f7;
  }
  * { box-sizing: border-box; margin: 0; padding: 0; }
  html, body {
    width: 1200px; height: 900px; overflow: hidden;
  }
  body {
    background: radial-gradient(ellipse at 60% 25%, var(--stage-light), var(--stage) 70%);
    font-family: "Arimo", Helvetica, Arial, sans-serif;
  }
  .folder {
    position: absolute; left: 170px; top: 150px;
    width: 860px; height: 600px;
    display: flex;
    box-shadow: 0 20px 40px rgba(0,0,0,0.25);
  }
  .panel {
    position: relative; width: 430px; height: 600px;
    background: var(--folder);
  }
  .panel--back { border-right: 1px solid var(--folder-edge); }
  .band {
    position: absolute; height: 14px;
    background: linear-gradient(90deg, var(--cyan), var(--cyan-deep));
  }
  .panel--back .band { left: 180px; right: 0; bottom: 118px; }
  .band--spine { left: 0; width: 8px; bottom: 118px; }
  .band--main {
    left: 200px; right: 0; bottom: 118px;
    display: flex; align-items: center; justify-content: flex-end;
    padding-right: 34px;
  }
  .band__url {
    font-size: 11px; color: var(--url-ink); letter-spacing: 0.5px;
  }
  .brand {
    position: absolute; left: 24px; bottom: 112px;
    display: flex; align-items: center; gap: 10px;
  }
  .brand__mark {
    width: 22px; height: 22px; background: var(--ink-light);
  }
  .brand__name {
    font-size: 17px; color: var(--cyan); letter-spacing: 0.5px;
  }
  .contact {
    position: absolute; left: 52px; bottom: 44px;
    padding-left: 12px;
    border-left: 1px solid var(--cyan-deep);
    color: var(--ink-light); font-size: 11px; line-height: 1.3;
  }
  .contact__group + .contact__group { margin-top: 8px; }
</style>
</head>
<body>
  <main class="folder" aria-label="VELKORIS presentation folder, outside spread">
    <section class="panel panel--back">
      <div class="band"></div>
      <address class="contact" style="font-style:normal">
        <div class="contact__group">
          <div>555-204-318</div>
          <div>dmarlow@velkoris.com</div>
          <div>www.velkoris.com</div>
        </div>
        <div class="contact__group">
          <div>18-42 Linden Street</div>
          <div>Brookvale, NY 11207</div>
        </div>
      </address>
    </section>
    <section class="panel panel--front">
      <div class="band band--spine"></div>
      <div class="brand">
        <span class="brand__mark"></span>
        <span class="brand__name">VELKORIS</span>
      </div>
      <div class="band band--main">
        <span class="band__url">www.velkoris.com</span>
      </div>
    </section>
  </main>
</body>
</html>
```